Business Consulting Company requires a website design (PSD+HTML+CSS required)

Tarnvale Advisory is a Business Consulting Company that provides Analysis, Business Coaching and Systems and Document Design for clients.

We would like a simplistic yet professional looking website design that uses high quality imagery to project a professional persona across our entire site.

The completed project will need to include PSD files (for editing in Photoshop) and will need to also include HTML+CSS coded files that can be edited in Adobe Dreamweaver CS5.5.

Tarnvale Advisory currently has a functioning website (located at www.tarnvaleadvisory.com.au) but would like to replace its current site with something more professional, user friendly and content simplistic, with the overall design of this project being clean and very easy to navigate whilst remaining professionally focused.

A brief has been attached to this project to provide the key details but please feel free to contact me if you require any clarification or have any questions regarding the project.

Target Market(s)

The target audience for this website will be small to medium sized businesses (of all descriptions).

Industry/Entity Type

Business

Coding

Coded - Design and coding required

Number of Pages Required

5+ page

Requirements
Must have
• Simplistic design structure
• Professional images
• Easy to navigate
• Must be uploaded in PSD format
• Must be coded (HTML+CSS) and compatible with Adobe Dreamweaver CS5.5
Nice to have
• Use of the Company’s corporate colours throughout the site design
• Adding a Home page slider bar with images and short catchy messages (i.e. text based statements)
• Having a quick link box on each page that provides easy navigation throughout the site
• The use of different icons and images to depict our different services (i.e. a different icon and image for analysis service and coaching service etc.).
• All pages should follow a similar theme (universal approach to all pages)
Should not have
• When coding, images should not be used in place of text (all text must be editable)

```html
<!DOCTYPE html>
<html lang="en">
<head>
<meta charset="utf-8">
<title>Tarnvale Advisory</title>
<link href="https://fonts.googleapis.com/css2?family=Source+Sans+3:wght@300;400;600;700&display=swap" rel="stylesheet">
<style>
:root{
  --blue:#0a8ccd;
  --blue-dark:#0677b3;
  --nav-blue:#2a9ad6;
  --ink:#333;
  --muted:#555;
  --page:#f2f2f2;
  --white:#fff;
  --footer:#333333;
  --footer-deep:#262626;
  --field:#f4f4f4;
}
*{margin:0;padding:0;box-sizing:border-box}
html,body{width:847px;height:1200px;overflow:hidden}
body{position:relative;background:var(--page);font-family:Arial,Helvetica,sans-serif;color:var(--ink)}
.abs{position:absolute}
.display{font-family:"Source Sans 3",Arial,sans-serif}

/* header */
.brand{left:72px;top:34px;display:flex;align-items:center;gap:10px;font-family:"Source Sans 3",Arial,sans-serif;font-weight:400;font-size:24px;color:#555;letter-spacing:1px}
.brand-dot{width:30px;height:30px;border-radius:50%;background:var(--blue)}
.main-nav{right:73px;top:45px;display:flex;font-family:"Source Sans 3",Arial,sans-serif;font-size:15px;font-weight:300;color:#444}
.main-nav span{padding:0 13px;border-left:1px solid #555;line-height:18px}
.main-nav span:first-child{border-left:0;color:var(--nav-blue);position:relative}
.main-nav span:last-child{padding-right:0}
.nav-caret{left:415px;top:66px}

/* hero */
.hero-frame{left:62px;top:110px;width:720px;height:274px;background:#fafafa;border:1px solid #ddd;box-shadow:0 1px 4px rgba(0,0,0,.15)}
.hero-photo{left:7px;top:10px;width:706px;height:256px;background:linear-gradient(120deg,#cfe2ec 0%,#e8eef1 40%,#9fb3c2 70%,#2b3440 100%)}

/* feature band */
.feature-band{left:0;top:405px;width:847px;height:299px;background:linear-gradient(#0a8fd2,#0783c4);box-shadow:inset 0 -12px 18px rgba(0,0,0,.12)}
.band-notch{left:424px;top:405px}
.feature{width:230px;text-align:center;color:var(--white)}
.feature-icon{width:66px;height:66px;border:3px solid var(--white);border-radius:50%;margin:0 auto;display:flex;align-items:center;justify-content:center}
.feature h2{font-family:"Source Sans 3",Arial,sans-serif;font-weight:300;font-size:22px;margin:14px 0 6px;letter-spacing:.5px}
.feature p{font-size:10.5px;line-height:14.5px;padding:0 8px}
.read-more{display:inline-block;margin-top:20px;border:1px solid var(--white);width:88px;height:28px;line-height:26px;font-family:"Source Sans 3",Arial,sans-serif;font-size:13px}

/* about */
.content{left:0;top:704px;width:847px;height:286px;background:var(--white)}
.about{left:85px;top:28px;width:445px}
.about h1,.testimonials h2{font-family:"Source Sans 3",Arial,sans-serif;font-weight:300;font-size:22px;color:#333}
.about p{font-size:10px;line-height:14.3px;color:var(--muted);margin-top:14px}
.about h1+p{margin-top:14px}
.divider{left:554px;top:16px;width:1px;height:200px;background:#e3e3e3}
.testimonials{left:572px;top:24px;width:190px}
.testimonials h3{font-family:"Source Sans 3",Arial,sans-serif;font-weight:600;font-size:12.5px;color:var(--blue);margin:6px 0 8px 5px}
.quote{font-size:9px;line-height:14px;color:#333;padding-left:4px}
.quote b{font-size:12px;vertical-align:-3px}
.signature{left:0;top:166px;width:147px;text-align:right;font-size:9px;line-height:13px;color:#444}
.signature strong{color:var(--blue)}
.avatar{left:156px;top:172px;width:28px;height:28px;border-radius:50%;background:linear-gradient(#c9b39b,#7d8b99);border:2px solid #eee}

/* footer */
.footer-rule{left:0;top:990px;width:847px;height:4px;background:var(--blue)}
.footer{left:0;top:994px;width:847px;height:169px;background:var(--footer);color:var(--white)}
.footer h4{font-family:"Source Sans 3",Arial,sans-serif;font-weight:700;font-size:12px;letter-spacing:.3px}
.links{left:112px;top:14px}
.links ul{list-style:none;margin-top:14px}
.links li{font-size:10px;line-height:17px;padding-left:9px;position:relative}
.links li::before{content:"";position:absolute;left:0;top:5px;border-left:4px solid var(--blue);border-top:3px solid transparent;border-bottom:3px solid transparent}
.contact{left:324px;top:14px}
.phone{display:flex;align-items:center;gap:5px;margin-top:16px;font-family:"Source Sans 3",Arial,sans-serif;font-weight:600;font-size:17px;letter-spacing:.5px;color:#e8e8e8}
.chat{left:0;top:82px;width:160px;height:28px;border-radius:4px;background:var(--blue);display:flex;align-items:center;font-size:9px;font-weight:bold}
.chat-label{flex:1;display:flex;align-items:center;gap:4px;padding-left:10px;border-right:1px solid rgba(255,255,255,.5);height:100%}
.chat-arrow{width:24px;text-align:center}
.social{left:4px;top:124px;display:flex;gap:11px}
.social i{width:8px;height:8px;border-radius:50%;background:var(--white);display:block}
.enquiry{left:588px;top:10px;width:130px}
.field{background:var(--field);height:22px;margin-top:2px;font-size:8px;color:#999;padding:6px 8px;border:1px solid #ddd}
.enquiry h4{margin-bottom:9px}
.field.message{height:45px}
.submit{margin:5px 0 0 70px;width:60px;height:19px;background:var(--blue);font-size:9px;text-align:center;line-height:19px}
.copyright{left:0;top:1163px;width:847px;height:37px;background:var(--footer-deep);color:#eee;font-size:8.5px;text-align:center;line-height:37px}
</style>
</head>
<body>

<header>
  <div class="abs brand"><span class="brand-dot"></span>TARNVALE ADVISORY</div>
  <nav class="abs main-nav"><span>HOME</span><span>about us</span><span>services</span><span>contact us</span><span>testimonials</span></nav>
  <svg class="abs nav-caret" width="10" height="6" viewBox="0 0 10 6"><path d="M1 1l4 4 4-4" fill="none" stroke="#2a9ad6" stroke-width="1.5"/></svg>
</header>

<div class="abs hero-frame">
  <div class="abs hero-photo" role="img" aria-label="Business team meeting around a bright office table"></div>
</div>

<section class="abs feature-band">
  <div class="abs feature" style="left:71px;top:38px">
    <div class="feature-icon">
      <svg width="34" height="34" viewBox="0 0 34 34" fill="#fff"><circle cx="13" cy="20" r="8"/><circle cx="13" cy="20" r="3" fill="#0a8cd0"/><circle cx="25" cy="10" r="6"/><circle cx="25" cy="10" r="2.2" fill="#0a8cd0"/></svg>
    </div>
    <h2>Services</h2>
    <p>Contrary to popular belief, Lorem Ipsum is not simply random text. It has roots in a piece of classical Latin literature from 45 BC, making it over 2000 years old.</p>
    <span class="read-more">Read More</span>
  </div>
  <div class="abs feature" style="left:318px;top:38px">
    <div class="feature-icon">
      <svg width="34" height="30" viewBox="0 0 34 30" fill="none" stroke="#fff" stroke-width="2.5" stroke-linejoin="round"><path d="M5 10h24v16H5z"/><path d="M5 10l5-7h14l5 7M17 10v16"/></svg>
    </div>
    <h2>Products</h2>
    <p>Contrary to popular belief, Lorem Ipsum is not simply random text. It has roots in a piece of classical Latin literature from 45 BC, making it over 2000 years old.</p>
    <span class="read-more">Read More</span>
  </div>
  <div class="abs feature" style="left:561px;top:44px">
    <div class="feature-icon">
      <svg width="38" height="24" viewBox="0 0 38 24" fill="#fff"><rect x="10" y="3" width="17" height="13"/><path d="M27 7h6l4 5v4H27z"/><circle cx="15" cy="18" r="3"/><circle cx="31" cy="18" r="3"/><rect x="1" y="6" width="7" height="2"/><rect x="3" y="10" width="5" height="2"/></svg>
    </div>
    <h2>Delivery Method</h2>
    <p>Contrary to popular belief, Lorem Ipsum is not simply random text. It has roots in a piece of classical Latin literature from 45 BC, making it over 2000 years old.</p>
    <span class="read-more">Read More</span>
  </div>
</section>
<svg class="abs band-notch" width="24" height="12" viewBox="0 0 24 12"><path d="M0 0h24L12 12z" fill="#f2f2f2"/></svg>

<section class="abs content">
  <div class="abs about">
    <h1>Making Business As Easy As Child’s Play!</h1>
    <p>Tarnvale Advisory is a Business Development and Consulting Company that provides affordable, high quality business solutions that are easy to understand and that are individually tailored to suit the needs of our clients.</p>
    <p>Understanding that each of our clients businesses are unique, Tarnvale works closely with our business partners to ensure the correct solutions are in place and that optimum efficiency is achieved.</p>
    <p>We focus on delivering immediate wins to guarantee value for money, all the while securing the transfer of essential skills and knowledge into the business, safeguarding a successful future for our clients.</p>
  </div>
  <div class="abs divider"></div>
  <div class="abs testimonials">
    <h2>Testimonials</h2>
    <h3>Director Corvell Pty Ltd.</h3>
    <p class="quote"><b>“</b> CORVELL recently engaged Tarnvale Advisory to assist with the immediate needs and the future development of our needs and the future developmentbusiness. At first I was a little sceptical as to what, if anything, Tarnvale would be able to help us with. Immediately they put my mind at ease... <b>”</b></p>
    <div class="abs signature">Martin J. Hollis - USA<br><strong>Brightwater Systems Corp</strong></div>
    <div class="abs avatar" role="img" aria-label="Client portrait"></div>
  </div>
</section>

<div class="abs footer-rule"></div>
<footer class="abs footer">
  <div class="abs links">
    <h4>LINKS</h4>
    <ul><li>Home</li><li>The Opportunity</li><li>The Challenge</li><li>The Solution</li><li>The Partner</li><li>Contact us</li></ul>
  </div>
  <div class="abs contact">
    <h4>CONTACT US</h4>
    <div class="phone">
      <svg width="17" height="17" viewBox="0 0 17 17"><rect width="17" height="17" rx="3" fill="#ccc"/><path d="M5 3l2 3-1 1.5c.7 1.6 1.9 2.8 3.5 3.5L11 10l3 2-1 2c-4.5-.2-8.8-4.5-9-9z" fill="#333"/></svg>
      +971 4210 6080
    </div>
    <div class="abs chat">
      <span class="chat-label"><svg width="14" height="12" viewBox="0 0 14 12"><path d="M7 1C3.7 1 1 3 1 5.5c0 1.3.7 2.4 1.8 3.2L2 11l3-1.5c.6.2 1.3.3 2 .3 3.3 0 6-2 6-4.5S10.3 1 7 1z" fill="none" stroke="#fff"/></svg>Live Chat - Online Now</span>
      <span class="chat-arrow">›</span>
    </div>
    <div class="abs social"><i></i><i></i><i></i></div>
  </div>
  <form class="abs enquiry">
    <h4>NEED MORE INFO ?</h4>
    <div class="field">Name</div>
    <div class="field">E-Mail</div>
    <div class="field message">Message</div>
    <div class="submit">Submit</div>
  </form>
</footer>
<div class="abs copyright">Copyright © 2014. Tarnvale Advisory. All rights reserved.</div>

</body>
</html>
```